"Dario Quillon" Business Card

Friends

My name is "Dario Quillon" and I need your help! I need a new business card for my personal use.

As background, "Dario Quillon" is actually an alias that I use when I meet women. Please use your creative skills to create an amazing business card for me to use!

In addition to including my name and contact details (see the "Must Have" section), you may wish to add a catchphrase or a title if you think it would help me :)

For background, please see:

http://www.dailybrightwire.com/2013/07/23/morton-feld-dario-quillon_n_5129847.html

Looking forward to seeing what you can do for me.

Hugs and kisses,

Dario Quillon [courtesy of PixelHarbor]

Target Market(s)

Adult women in New York City...or anywhere really.

Industry/Entity Type

Business

Requirements
Must have
• Please include the following details:

Dario Quillon
P: +1-555-3QUILLN
E: secrets@darioquillon-mail.com
Nice to have
• You might include a catchphrase, like "Quillon is my surname But you can call me Mr Smoothstep".

Or perhaps a title, like "Dario Quillon, Head of Sexy Times".

You're creative...I will leave the details to you my friends.
Should not have
• Any references to my actual name...because then, what's the point in using an alias?

```html
<!DOCTYPE html>
<html lang="en">
<head>
<meta charset="utf-8">
<title>Dario Quillon – Business Card</title>
<link href="https://fonts.googleapis.com/css2?family=Arimo:wght@400;700&display=swap" rel="stylesheet">
<style>
  :root {
    --ink-dark: #2b1e20;
    --ink-rust: #713320;
    --accent-orange: #f39223;
    --accent-brown: #6b3318;
    --rule-orange: #e8893a;
    --text-silver: #d6d3d3;
    --text-white: #ffffff;
    --paper: #ffffff;
    --ink-black: #111111;
  }
  * { margin: 0; padding: 0; box-sizing: border-box; }
  html, body {
    width: 1200px;
    height: 680px;
    overflow: hidden;
    background: var(--paper);
  }
  .card {
    position: relative;
    width: 1200px;
    height: 680px;
    overflow: hidden;
    font-family: "Arimo", Arial, sans-serif;
    background: var(--paper);
  }
  .card-front {
    position: absolute;
    left: 0; top: 0;
    width: 1200px;
    height: 503px;
    background: linear-gradient(to bottom, var(--ink-dark) 0%, #4a2620 45%, var(--ink-rust) 100%);
    border-bottom: 2px solid var(--rule-orange);
  }
  .droplet-layer {
    position: absolute;
    inset: 0;
    background: radial-gradient(ellipse at 20% 30%, rgba(255,255,255,0.04), transparent 60%);
  }
  .front-name {
    position: absolute;
    right: -22px;
    top: 146px;
    font-size: 54px;
    font-weight: 700;
    letter-spacing: 40px;
    color: var(--accent-orange);
    text-shadow: 3px 4px 6px rgba(0,0,0,0.55);
    white-space: nowrap;
  }
  .front-catchphrase {
    position: absolute;
    right: 11px;
    top: 214px;
    font-size: 33px;
    font-weight: 700;
    letter-spacing: 10px;
    color: var(--text-silver);
    white-space: nowrap;
  }
  .contact-list {
    position: absolute;
    left: 570px;
    top: 388px;
    list-style: none;
    font-size: 22px;
    line-height: 32px;
    color: var(--text-white);
  }
  .contact-label { color: var(--accent-orange); }
  .card-back-strip {
    position: absolute;
    left: 0; top: 505px;
    width: 1200px;
    height: 175px;
    background: var(--paper);
  }
  .strip-name {
    position: absolute;
    left: 10px;
    top: 14px;
    font-size: 68px;
    font-weight: 700;
    line-height: 1;
    background: linear-gradient(to bottom, var(--accent-orange) 0%, var(--accent-orange) 35%, var(--accent-brown) 100%);
    -webkit-background-clip: text;
    background-clip: text;
    color: transparent;
    filter: drop-shadow(3px 5px 3px rgba(0,0,0,0.45));
    white-space: nowrap;
  }
  .strip-title {
    position: absolute;
    left: 0;
    width: 1200px;
    top: 112px;
    text-align: center;
    font-size: 47px;
    letter-spacing: 10px;
    color: var(--ink-black);
    white-space: nowrap;
  }
</style>
</head>
<body>
  <main class="card">
    <section class="card-front">
      <div class="droplet-layer" role="img" aria-label="Water droplets scattered across the dark background"></div>
      <h1 class="front-name">DARIO QUILLON</h1>
      <p class="front-catchphrase">But you can call me Mr Smoothstep</p>
      <ul class="contact-list">
        <li><span class="contact-label">email:</span> secrets@darioquillon-mail.com</li>
        <li><span class="contact-label">phone:</span> +1-555-3QUILLN</li>
      </ul>
    </section>
    <section class="card-back-strip">
      <h2 class="strip-name">Dario Quillon</h2>
      <p class="strip-title">“Head of Sexy Times”</p>
    </section>
  </main>
</body>
</html>
```